A Healthy QORV Louisiana- TBLW Conference Poster

LA Carewell is presenting at the TBLW conference. The TBLW is a annual meeting for State, Federal and private sector individuals to provide opportunities for the exchange of ideas related to Carewell systems and heath policy affected by those systems. Louisiana will be presenting on their LaQORV Program . A poster with the information in the PowerPoint is needed. The first slide shows a draft of organization. The wording on slides two and three should be displayed in a visually appealing infographic. The charts should coordinate with the overall design. We would like to see the Louisiana state capital building incorporated.

Font styles to use
Sans Serif

Colors

Designer to choose colors to be used in the design.

Requirements
Must have
• Visually appealing infographics and charts
Nice to have
• Incorporate the capital building, incorporate the LaQORV logo (on first slide)

```html
<!DOCTYPE html>
<html lang="en">
<head>
<meta charset="utf-8">
<title>A Healthy QORV Louisiana</title>
<link href="https://fonts.googleapis.com/css2?family=Lato:wght@400;700;900&display=swap" rel="stylesheet">
<style>
:root{
  --backdrop:#d6d7d9;
  --sky-top:#2f84cc;
  --sky-mid:#5ea5dc;
  --sky-low:#a9d0ea;
  --panel:rgba(255,255,255,0.78);
  --panel-soft:rgba(255,255,255,0.62);
  --green:#5fb53a;
  --blue:#2d63ad;
  --head-blue:#4070b8;
  --ink:#2a2f3a;
  --row-a:#dfe5f1;
  --row-b:#eef1f7;
  --line:#2f6fb5;
  --grid:#9aa3ad;
}
*{box-sizing:border-box;margin:0;padding:0}
html,body{width:1200px;height:670px;overflow:hidden;background:var(--backdrop);font-family:"Lato",sans-serif;color:var(--ink)}
.poster{position:absolute;left:0;top:35px;width:1200px;height:600px;overflow:hidden;
  background:linear-gradient(180deg,var(--sky-top) 0%,var(--sky-mid) 45%,var(--sky-low) 80%)}
.capitol-photo{position:absolute;left:540px;top:46px;width:130px;height:440px;
  background:linear-gradient(180deg,#b9ab92 0%,#cbbfa6 50%,#a79a82 100%)}
.grounds-photo{position:absolute;left:0;top:470px;width:1200px;height:116px;
  background:linear-gradient(180deg,#6e9a55 0%,#4f8a3a 40%,#7cb553 100%)}
.base-strip{position:absolute;left:0;top:586px;width:1200px;height:14px;background:#fff}
.title{position:absolute;left:28px;top:46px;font-weight:900;font-size:42px;color:#fff;letter-spacing:-0.3px}
.intro{position:absolute;left:708px;top:52px;width:432px;text-align:center;color:#fff;font-size:7.6px;line-height:1.3}
.intro p+p{margin-top:7px}
.panel{position:absolute;background:var(--panel)}
.panel-obstacles{left:25px;top:134px;width:484px;height:233px}
.panel-solutions{left:691px;top:134px;width:484px;height:233px}
.panel-table-left{left:25px;top:397px;width:484px;height:142px;background:var(--panel-soft)}
.panel-table-right{left:691px;top:397px;width:484px;height:142px;background:var(--panel-soft)}
.panel-heading{position:absolute;top:22px;font-weight:900;font-size:13px;color:var(--green)}
.panel-obstacles .panel-heading{left:17px}
.panel-solutions .panel-heading{left:14px}
.points{position:absolute;font-size:6.4px;line-height:1.3}
.panel-obstacles .points{left:17px;top:46px;width:165px}
.panel-solutions .points{left:14px;top:51px;width:170px}
.point{margin-bottom:7px}
.point h3{font-size:6.4px;font-weight:700;color:var(--blue);text-transform:uppercase}
.logo-arch{position:absolute;left:480px;top:487px;width:240px;height:260px;border-radius:50%;background:#fff}
.logo-mark{position:absolute;left:480px;top:514px;width:240px;display:flex;justify-content:center;align-items:center;gap:8px}
.logo-square{width:22px;height:22px;background:var(--green)}
.logo-name{font-weight:700;font-size:30px;color:var(--blue)}
.data-table{position:absolute;border-collapse:collapse;font-size:6.4px;table-layout:fixed}
.data-table th{background:var(--head-blue);color:#fff;font-weight:400;text-align:left;padding:0 18px;height:12px}
.data-table td{padding:0 18px;border-right:1px solid #fff}
.data-table tr:nth-child(odd) td{background:var(--row-a)}
.data-table tr:nth-child(even) td{background:var(--row-b)}
.table-obstacles{left:43px;top:428px;width:446px}
.table-obstacles td{height:15.2px}
.table-solutions{left:709px;top:414px;width:447px}
.table-solutions td{height:15px}
.table-solutions tr.tall td{height:26px}
.charts{position:absolute;left:0;top:0;width:1200px;height:600px;pointer-events:none}
.charts text{font-family:"Lato",sans-serif;fill:var(--ink)}
.chart-title{font-size:9.5px;fill:var(--blue)!important}
.tick{font-size:6.5px}
.axis-name{font-size:6.3px}
.note{font-size:4.6px}
</style>
</head>
<body>
<div class="poster">
  <div class="capitol-photo" role="img" aria-label="Photograph of the Louisiana State Capitol tower"></div>
  <div class="grounds-photo" role="img" aria-label="Photograph of the capitol lawn, trees and flowering azaleas"></div>
  <div class="base-strip"></div>

  <h1 class="title">A Healthy QORV Louisiana</h1>
  <div class="intro">
    <p>Louisiana Quality Option Reimbursement Voucher (LaQORV) program allows for Carewell to pay the premium costs of member's private health insurance when cost effective for the State.</p>
    <p>To raise program participation the State is implementing strategic changes to increase enrollment by 95%, resulting in an $11.2M cost savings to the State by the end of SFY23.</p>
  </div>

  <section class="panel panel-obstacles">
    <h2 class="panel-heading">THE OBSTACLES:</h2>
    <div class="points">
      <div class="point"><h3>Budget Constraints</h3><p>Due to a budgetary shortfall the LaQORV program was discontinued on Dec 2015. By ending the program, all members were forced to cover their private insurance premiums, or switch to Carewell.</p></div>
      <div class="point"><h3>Lack of Public Knowledge</h3><p>Members are unaware that this program exists or find it hard to believe that Carewell will pay for their private health insurance.</p></div>
      <div class="point"><h3>Lack of Participation</h3><p>Cost effectiveness formula is too restrictive excluding a large portion of the viable population, including waiver, Fee for Service (FFS) members and the individual insurance market.</p></div>
      <div class="point"><h3>Crowd Out</h3><p>Crowd out occurs when members choose public insurance in lieu of available private health insurance.</p></div>
    </div>
  </section>

  <section class="panel panel-solutions">
    <h2 class="panel-heading">THE SOLUTIONS:</h2>
    <div class="points">
      <div class="point"><h3>Program Restored</h3><p>LaQORV was reinstated in April 2017, restoring LCD's focus on promoting employer-sponsored insurance.</p></div>
      <div class="point"><h3>Increase Awareness and Public Knowledge</h3><p>LCD has contracted a marketing firm to develop a comprehensive marketing and outreach strategy aimed at engaging providers, employers, insurance companies and members.</p></div>
      <div class="point"><h3>Increase Participation</h3><p>Refinement of the cost effectiveness formula increased the pool of members eligible for the program, including waiver, Fee for Service (FFS) members and the individual insurance market.</p></div>
      <div class="point"><h3>Data and Analytics</h3><p>The use of data mining identifies individuals and populations to be targeted for program outreach.</p></div>
    </div>
  </section>

  <div class="logo-arch"></div>
  <div class="logo-mark">
    <span class="logo-square"></span>
    <span class="logo-name">LaQORV</span>
  </div>

  <div class="panel panel-table-left"></div>
  <div class="panel panel-table-right"></div>

  <table class="data-table table-obstacles">
    <colgroup><col style="width:36%"><col style="width:36%"><col style="width:28%"></colgroup>
    <tr><th>Fiscal Year</th><th>Number of LaQORV Cases</th><th>Key Events</th></tr>
    <tr><td>FY12</td><td>0</td><td></td></tr>
    <tr><td>FY13</td><td>500</td><td></td></tr>
    <tr><td>FY14</td><td>1000</td><td></td></tr>
    <tr><td>FY15</td><td>1500</td><td>Funding Lost</td></tr>
    <tr><td>FY16</td><td>0</td><td></td></tr>
  </table>

  <table class="data-table table-solutions">
    <colgroup><col style="width:33.5%"><col style="width:33.5%"><col style="width:33%"></colgroup>
    <tr><th>Fiscal Year</th><th>Number of LaQORV Cases</th><th>Key Events</th></tr>
    <tr><td>FY17</td><td>0</td><td>Program Restored</td></tr>
    <tr><td>FY19</td><td>435</td><td>Current</td></tr>
    <tr class="tall"><td>FY20</td><td>566</td><td>Marketing Firm Engaged<br>Formula Refined</td></tr>
    <tr><td>FY21</td><td>848</td><td></td></tr>
    <tr><td>FY22</td><td>1,103</td><td></td></tr>
    <tr><td>FY23</td><td>1,434</td><td></td></tr>
  </table>

  <svg class="charts" viewBox="0 0 1200 600" aria-label="LaQORV participation charts">
    <g class="chart-obstacles">
      <text class="chart-title" x="353" y="182" text-anchor="middle">LaQORV Participation</text>
      <g stroke="var(--grid)" stroke-width="0.6">
        <line x1="260" y1="193" x2="486" y2="193"/><line x1="260" y1="206.75" x2="486" y2="206.75"/>
        <line x1="260" y1="220.5" x2="486" y2="220.5"/><line x1="260" y1="234.25" x2="486" y2="234.25"/>
        <line x1="260" y1="248" x2="486" y2="248"/><line x1="260" y1="261.75" x2="486" y2="261.75"/>
        <line x1="260" y1="275.5" x2="486" y2="275.5"/><line x1="260" y1="289.25" x2="486" y2="289.25"/>
        <line x1="260" y1="303" x2="486" y2="303"/>
      </g>
      <g class="tick" text-anchor="end">
        <text x="248" y="195">1600</text><text x="248" y="209">1400</text><text x="248" y="223">1200</text>
        <text x="248" y="236">1000</text><text x="248" y="250">800</text><text x="248" y="264">600</text>
        <text x="248" y="278">400</text><text x="248" y="291">200</text><text x="248" y="305">0</text>
      </g>
      <g class="tick" text-anchor="middle" style="font-size:5px">
        <text x="275" y="313">FY12</text><text x="322" y="313">FY13</text><text x="370" y="313">FY14</text>
        <text x="417" y="313">FY15</text><text x="463" y="313">FY16</text>
      </g>
      <text class="axis-name" x="353" y="324" text-anchor="middle">Fiscal Year</text>
      <text class="axis-name" transform="translate(228 248) rotate(-90)" text-anchor="middle">Number of LaQORV Cases</text>
      <polyline points="275,303 417,199.9 463,303" fill="none" stroke="var(--line)" stroke-width="1.4"/>
    </g>
    <g class="chart-solutions">
      <text class="chart-title" x="1019" y="178" text-anchor="middle">LaQORV Participation</text>
      <g stroke="var(--grid)" stroke-width="0.6">
        <line x1="918" y1="189" x2="1157" y2="189"/><line x1="918" y1="203.5" x2="1157" y2="203.5"/>
        <line x1="918" y1="218" x2="1157" y2="218"/><line x1="918" y1="232.5" x2="1157" y2="232.5"/>
        <line x1="918" y1="247" x2="1157" y2="247"/><line x1="918" y1="261.5" x2="1157" y2="261.5"/>
        <line x1="918" y1="276" x2="1157" y2="276"/><line x1="918" y1="290.5" x2="1157" y2="290.5"/>
        <line x1="918" y1="305" x2="1157" y2="305"/>
      </g>
      <g class="tick" text-anchor="end">
        <text x="908" y="191">1600</text><text x="908" y="206">1400</text><text x="908" y="220">1200</text>
        <text x="908" y="235">1000</text><text x="908" y="249">800</text><text x="908" y="264">600</text>
        <text x="908" y="278">400</text><text x="908" y="293">200</text><text x="908" y="307">0</text>
      </g>
      <g class="tick" text-anchor="middle" style="font-size:5px">
        <text x="936" y="315">FY17</text><text x="976" y="315">FY19</text><text x="1017" y="315">FY20</text>
        <text x="1057" y="315">FY21</text><text x="1098" y="315">FY22</text><text x="1137" y="315">FY23</text>
      </g>
      <text class="axis-name" x="1037" y="327" text-anchor="middle">Fiscal Year</text>
      <text class="axis-name" transform="translate(886 247) rotate(-90)" text-anchor="middle">Number of LaQORV Cases</text>
      <polyline points="936,305 976,273.5 1017,264 1057,243.5 1098,225 1137,201" fill="none" stroke="var(--line)" stroke-width="1.2"/>
      <g fill="var(--line)">
        <circle cx="936" cy="305" r="1.9"/><circle cx="976" cy="273.5" r="1.9"/><circle cx="1017" cy="264" r="1.9"/>
        <circle cx="1057" cy="243.5" r="1.9"/><circle cx="1098" cy="225" r="1.9"/><circle cx="1137" cy="201" r="1.9"/>
      </g>
      <g class="note" text-anchor="middle">
        <text x="929" y="290">Program</text><text x="929" y="295">Restored</text>
        <text x="972" y="268">Current</text>
        <text x="1020" y="247">Marketing Firm</text><text x="1020" y="252">Engaged</text>
        <text x="1040" y="266">Formula</text><text x="1040" y="271">Refined</text>
      </g>
    </g>
  </svg>
</div>
</body>
</html>
```